Illustrate a statistic and its significance

Please create a graphical representation of the success rate of the Vail Procedure for our website. The Vail Procedure has a success rate of 80%. This means the procedure is successful for 8 out of every 10 people. An 80% success rate by itself is great. However, it's even more impressive when you consider that the only people we perform this procedure on are patients who have exhausted conventional treatment options for migraines and headaches. I would really like to emphasize both the success rate and the type of patients we are successful in treating with this procedure.
For example, you could create an illustration of outlines of 10 people with 8 of them shaded in, which would represent an 80% success rate. Then, underneath this image, you could add a bullet list of the types of treatments patients (such as the 10 figures in the image) have tried before coming to us/having this procedure, which include the following:
Prescription medications
Trigger point injections
Nerve blocks
Migraine surgery
Dermil
Chiropractic care
Physical therapy
Biofeedback
Massage
Acupuncture
Or maybe there is another/better way to represent this statistic graphically? I'm just looking for an effective illustration of this important statistic and its significance.
Our brand colors are red (#fd444a) and blue (#214170)
Thank you!
People who suffer from chronic migraines and headaches
Healthcare/Medical
- Athiti

```html
<!DOCTYPE html>
<html lang="en">
<head>
<meta charset="utf-8">
<title>Vail Procedure – 80% Success</title>
<link rel="stylesheet" href="https://fonts.googleapis.com/css2?family=PT+Sans:wght@400;700&display=swap">
<style>
  :root {
    --brand-red: #ef464d;
    --brand-blue: #1e3f6f;
    --tile-grey: #d1d3d4;
    --ink: #1b1b1b;
    --white: #ffffff;
  }
  * { box-sizing: border-box; margin: 0; padding: 0; }
  html, body {
    width: 1164px;
    height: 1200px;
    overflow: hidden;
    background: var(--white);
  }
  .infographic {
    position: relative;
    width: 1164px;
    height: 1200px;
    font-family: "PT Sans", sans-serif;
  }
  .banner {
    position: absolute;
    top: 103px;
    height: 95px;
    border-radius: 28px;
    display: flex;
    align-items: center;
    justify-content: center;
    font-weight: 700;
    font-size: 58px;
    letter-spacing: -1px;
    line-height: 1;
    text-transform: uppercase;
  }
  .banner--name {
    left: 38px;
    width: 529px;
    background: var(--brand-blue);
    color: var(--brand-red);
  }
  .banner--stat {
    left: 600px;
    width: 525px;
    background: var(--brand-red);
    color: var(--brand-blue);
  }
  .patient {
    position: absolute;
    width: 195px;
    height: 195px;
    border-radius: 30px;
    overflow: hidden;
    border: 2px solid var(--brand-red);
  }
  .patient--helped {
    background: radial-gradient(ellipse 45% 60% at 50% 72%, var(--brand-blue) 0%, var(--brand-blue) 55%, var(--tile-grey) 100%);
  }
  .patient--other {
    border-color: var(--brand-blue);
    background: radial-gradient(ellipse 45% 60% at 50% 72%, var(--brand-red) 0%, var(--brand-red) 55%, var(--white) 100%);
  }
  .row-1 { top: 219px; }
  .row-2 { top: 435px; }
  .col-1 { left: 40px; }
  .col-2 { left: 264px; }
  .col-3 { left: 486px; }
  .col-4 { left: 710px; }
  .col-5 { left: 932px; }

  .treatments {
    position: absolute;
    left: 376px;
    top: 672px;
    width: 448px;
    height: 455px;
    border: 2px solid var(--brand-blue);
    border-top: none;
    border-radius: 0 0 44px 44px;
    background: var(--white);
  }
  .treatments__title {
    height: 58px;
    margin: 0 -2px;
    background: var(--brand-red);
    border: 2px solid var(--brand-blue);
    border-bottom: none;
    color: var(--white);
    font-weight: 400;
    font-size: 33px;
    line-height: 58px;
    text-align: center;
    letter-spacing: -0.5px;
  }
  .treatments__list {
    list-style: none;
    padding: 18px 0 0 79px;
  }
  .treatments__item {
    display: flex;
    align-items: center;
    height: 37px;
    font-weight: 700;
    font-size: 25px;
    color: var(--ink);
    letter-spacing: -0.2px;
  }
  .treatments__mark {
    width: 22px;
    height: 22px;
    margin-right: 11px;
    flex: none;
  }
</style>
</head>
<body>
<main class="infographic">
  <h1 class="banner banner--name">Vail Procedure</h1>
  <p class="banner banner--stat">80% Success</p>

  <section class="patients" aria-label="8 out of 10 patients helped">
    <div class="patient patient--helped row-1 col-1" role="img" aria-label="Silhouette of a patient helped by the procedure"></div>
    <div class="patient patient--helped row-1 col-2" role="img" aria-label="Silhouette of a patient helped by the procedure"></div>
    <div class="patient patient--helped row-1 col-3" role="img" aria-label="Silhouette of a patient helped by the procedure"></div>
    <div class="patient patient--helped row-1 col-4" role="img" aria-label="Silhouette of a patient helped by the procedure"></div>
    <div class="patient patient--helped row-1 col-5" role="img" aria-label="Silhouette of a patient helped by the procedure"></div>
    <div class="patient patient--helped row-2 col-1" role="img" aria-label="Silhouette of a patient helped by the procedure"></div>
    <div class="patient patient--helped row-2 col-2" role="img" aria-label="Silhouette of a patient helped by the procedure"></div>
    <div class="patient patient--helped row-2 col-3" role="img" aria-label="Silhouette of a patient helped by the procedure"></div>
    <div class="patient patient--other row-2 col-4" role="img" aria-label="Silhouette of a patient not helped"></div>
    <div class="patient patient--other row-2 col-5" role="img" aria-label="Silhouette of a patient not helped"></div>
  </section>

  <section class="treatments">
    <h2 class="treatments__title">UNSUCCESFUL TREATMENTS</h2>
    <ul class="treatments__list">
      <li class="treatments__item"><svg class="treatments__mark" viewBox="0 0 22 22" aria-hidden="true"><rect width="22" height="22" fill="#ef464d"/><path d="M6 4 L16 18 M16 4 L6 18" stroke="#fff" stroke-width="3"/></svg>Prescription medications</li>
      <li class="treatments__item"><svg class="treatments__mark" viewBox="0 0 22 22" aria-hidden="true"><rect width="22" height="22" fill="#ef464d"/><path d="M6 4 L16 18 M16 4 L6 18" stroke="#fff" stroke-width="3"/></svg>Trigger point injections</li>
      <li class="treatments__item"><svg class="treatments__mark" viewBox="0 0 22 22" aria-hidden="true"><rect width="22" height="22" fill="#ef464d"/><path d="M6 4 L16 18 M16 4 L6 18" stroke="#fff" stroke-width="3"/></svg>Nerve blocks</li>
      <li class="treatments__item"><svg class="treatments__mark" viewBox="0 0 22 22" aria-hidden="true"><rect width="22" height="22" fill="#ef464d"/><path d="M6 4 L16 18 M16 4 L6 18" stroke="#fff" stroke-width="3"/></svg>Migraine surgery</li>
      <li class="treatments__item"><svg class="treatments__mark" viewBox="0 0 22 22" aria-hidden="true"><rect width="22" height="22" fill="#ef464d"/><path d="M6 4 L16 18 M16 4 L6 18" stroke="#fff" stroke-width="3"/></svg>Dermil</li>
      <li class="treatments__item"><svg class="treatments__mark" viewBox="0 0 22 22" aria-hidden="true"><rect width="22" height="22" fill="#ef464d"/><path d="M6 4 L16 18 M16 4 L6 18" stroke="#fff" stroke-width="3"/></svg>Chiropractic care</li>
      <li class="treatments__item"><svg class="treatments__mark" viewBox="0 0 22 22" aria-hidden="true"><rect width="22" height="22" fill="#ef464d"/><path d="M6 4 L16 18 M16 4 L6 18" stroke="#fff" stroke-width="3"/></svg>Physical therapy</li>
      <li class="treatments__item"><svg class="treatments__mark" viewBox="0 0 22 22" aria-hidden="true"><rect width="22" height="22" fill="#ef464d"/><path d="M6 4 L16 18 M16 4 L6 18" stroke="#fff" stroke-width="3"/></svg>Biofeedback</li>
      <li class="treatments__item"><svg class="treatments__mark" viewBox="0 0 22 22" aria-hidden="true"><rect width="22" height="22" fill="#ef464d"/><path d="M6 4 L16 18 M16 4 L6 18" stroke="#fff" stroke-width="3"/></svg>Massage</li>
      <li class="treatments__item"><svg class="treatments__mark" viewBox="0 0 22 22" aria-hidden="true"><rect width="22" height="22" fill="#ef464d"/><path d="M6 4 L16 18 M16 4 L6 18" stroke="#fff" stroke-width="3"/></svg>Acupuncture</li>
    </ul>
  </section>
</main>
</body>
</html>
```